It is a leisure sector investment company.The company plans to invest in a luxurious 5 star resort

We need a stationery design to our company 'Copper Lantern Limited' using the winning logo design. We need the letter heads, envelopes & the business cards. Should be simple, plain and professional
We have upload the source file & vector files which gives our logo design. We prefer the bottom logo.

Have updated under 'must have priorities', the company name, address, tel no. fax no. & the company reg no. which should come on the letter head. the long envelope should have the company name, tel & fax no. 
Business card should have the company name, name on the card, designation, tel no. fax no.  

- Letter head details:
Copper Lantern Limited
14 Floor, South Wing, Halvard Merchant Plaza,
Merrow Court, Colombo 01, Sri Lanka
Tel: +94 11 5047293 Fax: +94 11 5047298
Company Reg No.QX 6142
Long Envelope should have only the company name, adress, Tel & Fax
Business Cards should have the company name, Tel & Fax:
Business Card 1 - Lasantha Gunaratne - Chairman
Business Card 2 - Nimal.T.Wijesooriya - COO

```html
<!DOCTYPE html>
<html lang="en">
<head>
<meta charset="utf-8">
<title>Copper Lantern Limited – Stationery Set</title>
<link href="https://fonts.googleapis.com/css2?family=Open+Sans:wght@400;600&display=swap" rel="stylesheet">
<style>
  :root{
    --bg:#2b2b2b;
    --paper:#ffffff;
    --ink:#1e1e1e;
    --ink-mid:#555555;
    --ink-light:#8a8a8a;
    --rule:#bdbdbd;
    --band:#e6e6e6;
    --ornament-a:#f3f3f3;
    --ornament-b:#e9e9e9;
  }
  *{margin:0;padding:0;box-sizing:border-box}
  html,body{width:1200px;height:900px;overflow:hidden}
  body{background:var(--bg);font-family:"Open Sans",Arial,sans-serif;color:var(--ink);position:relative}
  .sheet{position:absolute;background:var(--paper);box-shadow:0 3px 14px rgba(0,0,0,.45);overflow:hidden}
  .brand{position:absolute;display:flex;align-items:center;gap:.5em;font-weight:600;color:var(--ink);text-transform:uppercase;letter-spacing:.03em;white-space:nowrap}
  .brand .dot{width:.55em;height:.55em;border-radius:50%;background:var(--ink);flex:none}
  .brand .name{display:block;text-align:center;line-height:1.05}
  .contact{position:absolute;border-left:1px solid var(--rule);color:var(--ink-light);line-height:1.3;font-style:normal;white-space:nowrap}
  .contact .gap{display:block;height:.5em}
  .faint-decor{position:absolute;background:radial-gradient(ellipse at center,var(--ornament-b) 0%,var(--ornament-a) 55%,rgba(255,255,255,0) 80%)}
  .footer-rule{position:absolute;height:1px;background:var(--rule)}
  .reg{position:absolute;color:var(--ink-light);text-align:center}

  /* letterhead back sheet */
  .letterhead-back{left:40px;top:35px;width:615px;height:820px}
  .letterhead-back .brand{left:62px;top:62px;font-size:20px}
  .letterhead-back .contact{left:420px;top:50px;padding-left:12px;font-size:8.5px}
  .letterhead-back .faint-decor{left:30px;top:560px;width:560px;height:240px}
  .letterhead-back .footer-rule{left:140px;top:787px;width:385px}
  .letterhead-back .reg{left:140px;top:798px;width:385px;font-size:6px}

  /* letter front */
  .letter{left:290px;top:205px;width:445px;height:575px}
  .letter .brand{left:28px;top:48px;font-size:14px}
  .letter .contact{left:290px;top:26px;padding-left:7px;font-size:5.4px}
  .letter .salutation{position:absolute;left:58px;top:140px;font-size:8px;font-weight:600}
  .letter .body{position:absolute;left:58px;top:160px;width:332px;font-size:5.6px;line-height:1.34;text-align:justify;color:var(--ink)}
  .letter .body p{margin-bottom:26px}
  .letter .faint-decor{left:30px;top:400px;width:390px;height:150px}
  .letter .signature{position:absolute;left:225px;top:472px;width:150px;height:36px;background:linear-gradient(90deg,rgba(60,60,60,.12),rgba(60,60,60,.25),rgba(60,60,60,.12));border-radius:3px}
  .letter .role{position:absolute;left:268px;top:512px;font-size:7px}
  .letter .footer-rule{left:88px;top:557px;width:277px}
  .letter .reg{left:88px;top:563px;width:277px;font-size:4px}

  /* envelope */
  .envelope{left:768px;top:38px;width:372px;height:162px}
  .envelope .brand{left:16px;top:20px;font-size:9.5px}
  .envelope .window{position:absolute;left:16px;top:62px;width:152px;height:54px;border:1px solid #c8c8c8;border-radius:6px;box-shadow:0 2px 5px rgba(0,0,0,.35);background:var(--paper)}
  .envelope .contact{left:18px;top:128px;padding-left:5px;font-size:4.3px}
  .envelope .faint-decor{left:180px;top:55px;width:180px;height:105px}

  /* fax */
  .fax{left:778px;top:240px;width:362px;height:440px}
  .fax .brand{left:16px;top:20px;font-size:8.5px;letter-spacing:.02em}
  .fax .title{position:absolute;left:122px;top:18px;font-size:21px;font-weight:600;letter-spacing:.02em;color:#3a3a3a}
  .fax .contact{left:235px;top:19px;padding-left:5px;font-size:4.5px}
  .fax .fields{position:absolute;left:0;top:58px;width:100%;height:70px;background:var(--band);font-size:7px;color:var(--ink-mid)}
  .fax .field{position:absolute}
  .fax .field span{position:absolute;left:38px}
  .fax .field.right span{left:57px}

  /* business cards */
  .card{width:275px;height:165px;background:linear-gradient(180deg,#f7f7f7,#e4e4e4)}
  .card-back{left:905px;top:700px}
  .card-back .brand{left:62px;top:58px;font-size:12px}
  .card-back .reflection{position:absolute;left:76px;top:88px;width:140px;height:14px;background:linear-gradient(180deg,rgba(0,0,0,.08),rgba(0,0,0,0))}
  .card-back .reg{left:0;top:150px;width:100%;font-size:4.5px}
  .card-front{left:815px;top:582px}
  .card-front .brand{left:10px;top:12px;font-size:10px}
  .card-front .person{position:absolute;left:56px;top:70px;font-size:7.5px;font-weight:600}
  .card-front .title{position:absolute;left:56px;top:82px;font-size:5.5px;color:var(--ink-mid)}
  .card-front .contact{left:142px;top:104px;border:none;font-size:5px;color:var(--ink-mid);line-height:1.45}
  .card-front .faint-decor{left:0;top:40px;width:120px;height:125px}
</style>
</head>
<body>

<section class="sheet letterhead-back" aria-label="Letterhead">
  <div class="brand"><span class="dot"></span><span class="name">Copper Lantern<br>Limited</span></div>
  <address class="contact">14 Floor, South Wing, Halvard Merchant Plaza,<br>Merrow Court, Colombo 01, Sri Lanka<span class="gap"></span>Tel &nbsp;&nbsp;: +94 11 5047293<br>Fax &nbsp;: +94 11 5047298</address>
  <div class="faint-decor" role="img" aria-label="Faint decorative emblem watermark"></div>
  <div class="footer-rule"></div>
  <div class="reg">Company Reg No.QX 6142</div>
</section>

<section class="sheet letter" aria-label="Letter">
  <div class="brand"><span class="dot"></span><span class="name">Copper Lantern<br>Limited</span></div>
  <address class="contact">14 Floor, South Wing, Halvard Merchant Plaza,<br>Merrow Court, Colombo 01, Sri Lanka<span class="gap"></span>Tel &nbsp;: +94 11 5047293<br>Fax : +94 11 5047298</address>
  <div class="faint-decor" role="img" aria-label="Faint decorative emblem watermark"></div>
  <div class="salutation">Dear Costumer.</div>
  <div class="body">
    <p>Fusce suscipit varius mi. Cum sociis natoque penatibus et magnis dis parturient montes, nascetur ridiculus mus. Nulla dui. Morbi nunc odio, gravida at, cursus nec, luctus a, lorem.Maecenas tristique orci ac sem. Duis ultricies pharetra agna. Donec accumsan malesuada orci. Donec sit amet eros. Lorem ipsum dolor sit amet, consectetuer adipiscing elit. Mauris fermentum dictum magna. Sed laoreet aliquam leo. Ut tellus dolor, dapibus eget, elementum vel, cursus eleifend, elit. Aenean auctor wisi et urna. Non numquam eius modi tempora incidunt ut labore et dolore magnam aliquam quaerat voluptatem. Ut enim ad minima veniam, quis exer. Fusce suscipit varius mi. Cum sociis natoque penatibus et magnis dis parturient montes, nascetur ridiculus mus. Nulla dui. Morbi nunc odio, gravida at, cursus nec, luctus a, lorem.Maecenas tristique orci ac sem. Duis ultricies pharetra agna. Donec accumsan malesuada orci. Donec sit amet eros. Lorem ipsum dolor sit amet, consectetuer adipiscing elit. Mauris fermentum dictum magna. Sed laoreet aliquam leo. Ut tellus dolor, dapibus eget, elementum vel, cursus eleifend, elit. Aenean auctor wisi et urna. Non numquam eius modi tempora incidunt ut labore et dolore magnam aliquam quaerat voluptatem. Ut enim ad minima veniam, quis exer.</p>
    <p>Fusce suscipit varius mi. Cum sociis natoque penatibus et magnis dis parturient montes, nascetur ridiculus mus. Nulla dui. Morbi nunc odio, gravida at, cursus nec, luctus a, lorem.Maecenas tristique orci ac sem. Duis ultricies pharetra agna. Donec accumsan malesuada orci. Donec sit amet eros. Lorem ipsum dolor sit amet, consectetuer adipiscing elit. Mauris fermentum dictum magna. Sed laoreet aliquam leo. Ut tellus dolor, dapibus eget, elementum vel, cursus eleifend, elit. Aenean auctor wisi et urna. Non numquam eius modi tempora incidunt ut labore et dolore magnam aliquam quaerat voluptatem. Ut enim ad minima veniam, quis exer.</p>
    <p>Fusce suscipit varius mi. Cum sociis natoque penatibus et magnis dis parturient montes, nascetur ridiculus mus. Nulla dui. Morbi nunc odio, gravida at, cursus nec, luctus a, lorem.Maecenas tristique orci ac sem. Duis ultricies pharetra agna. Donec accumsan malesuada orci. Donec sit amet eros. Lorem ipsum dolor sit amet, consectetuer adipiscing elit. Mauris fermentum dictum magna. Sed laoreet aliquam leo. Ut tellus dolor, dapibus eget, elementum vel, cursus eleifend, elit. Aenean auctor wisi et urna. Non numquam eius modi tempora incidunt ut labore et dolore magnam aliquam quaerat voluptatem. Ut enim ad minima veniam, quis exer. Fusce suscipit varius mi. Cum sociis natoque penatibus et magnis dis parturient montes, nascetur ridiculus mus. Nulla dui. Morbi nunc odio, gravida at, cursus nec, luctus a, lorem.Maecenas tristique orci ac sem. Duis ultricies pharetra agna. Donec accumsan malesuada orci. Donec sit amet eros. Lorem ipsum dolor sit amet, consectetuer adipiscing elit. Mauris fermentum dictum magna. Sed laoreet aliquam leo. Ut tellus dolor, dapibus eget, elementum vel, cursus eleifend, elit. Aenean auctor wisi et urna. Non numquam eius modi tempora incidunt ut labore et dolore magnam aliquam quaerat voluptatem. Ut enim ad minima veniam, quis exer.</p>
  </div>
  <div class="signature" role="img" aria-label="Handwritten signature of Ravi K. Mendis"></div>
  <div class="role">CEO manager</div>
  <div class="footer-rule"></div>
  <div class="reg">Company Reg No.QX 6142</div>
</section>

<section class="sheet envelope" aria-label="Long envelope">
  <div class="brand"><span class="dot"></span><span class="name">Copper Lantern<br>Limited</span></div>
  <div class="window"></div>
  <address class="contact">14 Floor, South Wing, Halvard Merchant Plaza,<br>Merrow Court, Colombo 01, Sri Lanka<span class="gap"></span>Tel &nbsp;: +94 11 5047293<br>Fax : +94 11 5047298</address>
  <div class="faint-decor" role="img" aria-label="Faint decorative emblem watermark"></div>
</section>

<section class="sheet fax" aria-label="Fax cover sheet">
  <div class="brand"><span class="dot"></span><span class="name">Copper Lantern<br>Limited</span></div>
  <div class="title">FAX</div>
  <address class="contact">14 Floor, South Wing, Halvard Merchant Plaza,<br>Merrow Court, Colombo 01, Sri Lanka<br>Tel &nbsp;: +94 11 5047293<br>Fax : +94 11 5047298</address>
  <div class="fields">
    <div class="field" style="left:27px;top:10px">Date<span>:</span></div>
    <div class="field" style="left:27px;top:32px">Attention<span>:</span></div>
    <div class="field" style="left:27px;top:53px">From<span>:</span></div>
    <div class="field right" style="left:180px;top:10px">Regarding<span>:</span></div>
    <div class="field right" style="left:180px;top:32px">Pages<span>:</span></div>
    <div class="field right" style="left:180px;top:53px">Including cover<span>:</span></div>
  </div>
</section>

<section class="sheet card card-back" aria-label="Business card back">
  <div class="brand"><span class="dot"></span><span class="name">Copper Lantern<br>Limited</span></div>
  <div class="reflection"></div>
  <div class="reg">Company Reg No.QX 6142</div>
</section>

<section class="sheet card card-front" aria-label="Business card front">
  <div class="faint-decor" role="img" aria-label="Faint decorative emblem watermark"></div>
  <div class="brand"><span class="dot"></span><span class="name">Copper Lantern<br>Limited</span></div>
  <div class="person">Lasantha Gunaratne</div>
  <div class="title">Chairman</div>
  <address class="contact">14 Floor, South Wing, Halvard Merchant Plaza,<br>Merrow Court, Colombo 01, Sri Lanka<br>Mobile &nbsp;: +94 77 618 3520<br>Tel &nbsp;&nbsp;&nbsp;&nbsp;&nbsp;&nbsp;: +94 11 5047293<br>Fax &nbsp;&nbsp;&nbsp;&nbsp;&nbsp;&nbsp;: +94 11 5047298</address>
</section>

</body>
</html>
```